Corporate Profile

We are an Electrical Engineering company and we require a rework on our company profile urgently. We need it be have a nice modern look and feel.

We do not have much time as we need the brochures ready printed before 24th Oct 2014.

Please find attached a .pdf file with our company profile and a complimetary slip that has our high definition logo to be extracted.

1. We require a front page design. 2. There is no particular size. You can suggest on the size.

Electrical

```html
<!DOCTYPE html>
<html lang="en">
<head>
<meta charset="utf-8">
<title>Voltridge Power – Company Profile 05</title>
<link href="https://fonts.googleapis.com/css2?family=Arimo:wght@400;700&family=Open+Sans:wght@400;700&family=Roboto+Condensed:wght@400;700&display=swap" rel="stylesheet">
<style>
  :root{
    --backdrop:#1c1c1c;
    --paper:#ffffff;
    --haze:#e9e9e4;
    --brand-red:#d8072a;
    --ink:#1a1a1a;
    --grid:#9a9a9a;
    --line-blue:#1a22d6;
    --line-green:#22c81e;
    --line-brown:#7a2a12;
    --line-magenta:#e01ad8;
    --line-cyan:#19d0e0;
    --photo-orange:#d9673a;
    --photo-grey:#cfd2d2;
    --photo-steel:#9aa3a2;
  }
  *{margin:0;padding:0;box-sizing:border-box}
  html,body{width:998px;height:1200px;overflow:hidden;background:var(--backdrop)}
  .page{position:absolute;left:93px;top:74px;width:812px;height:1050px;background:var(--paper);overflow:hidden}
  .page-haze{position:absolute;left:0;top:112px;width:100%;height:260px;background:linear-gradient(to bottom,var(--haze),var(--paper))}
  .accent-tab{position:absolute;left:583px;top:0;width:170px;height:8px;background:var(--brand-red)}
  .brand{position:absolute;left:57px;top:36px;display:flex;align-items:center;gap:8px;font-family:"Arimo",Arial,sans-serif;font-weight:700;font-size:17px;color:var(--brand-red);letter-spacing:.5px}
  .brand-mark{width:14px;height:14px;background:var(--brand-red)}
  .contact{position:absolute;right:20px;top:20px;text-align:right;font-family:"Arimo",Arial,sans-serif;font-size:7.3px;line-height:9.6px;color:var(--ink)}
  .contact .company{font-weight:700}
  .panels{position:absolute;top:202px;left:74px;width:662px}
  .panel-photo{position:absolute;top:0;width:191px;height:214px;border-radius:6px}
  .panel-photo.mcc{left:0;background:linear-gradient(135deg,var(--photo-orange),#a8472a 60%,#6d7d86)}
  .panel-photo.pcc{left:233px;width:190px;background:linear-gradient(160deg,#eeeeee,var(--photo-grey))}
  .panel-photo.automation{left:470px;background:linear-gradient(120deg,var(--photo-steel),#6e7574 55%,#b9c0bf)}
  .caption{position:absolute;top:250px;width:191px;text-align:center;font-family:"Open Sans",Arial,sans-serif;font-weight:700;font-size:12px;color:var(--ink)}
  .caption.mcc{left:0}.caption.pcc{left:233px}.caption.automation{left:470px}
  .analysis-chart{position:absolute;left:70px;top:509px;width:606px;height:351px}
  .analysis-caption{position:absolute;left:0;top:880px;width:100%;text-align:center;font-family:"Open Sans",Arial,sans-serif;font-weight:700;font-size:12px;color:var(--ink)}
  .footer-band{position:absolute;left:0;top:976px;width:100%;height:54px;background:var(--brand-red)}
  .footer-label{position:absolute;right:112px;top:14px;font-family:"Roboto Condensed",Arial,sans-serif;font-size:18px;color:#fff;letter-spacing:.3px}
  .footer-label b{font-weight:700;margin-left:4px}
  .footer-label .sep{margin:0 8px}
  .chart-text{font-family:"Arimo",Arial,sans-serif;font-size:5px;fill:#333}
</style>
</head>
<body>
<div class="page">
  <div class="page-haze"></div>
  <div class="accent-tab"></div>
  <div class="brand"><span class="brand-mark"></span>VOLTRIDGE POWER</div>
  <div class="contact">
    <div class="company">VOLTRIDGE ELECTRICAL &amp; SUPPLIES LIMITED</div>
    <div>P.O. BOX 21530 – 00200, CITY SQUARE, NAIROBI, KENYA.</div>
    <div>TEL (INDUSTRIAL AREA): +254 (20) 5550143/4, 5550199</div>
    <div>TEL (TOWN OFFICE): +254 (20) 5550712/5550718</div>
    <div>FAX (INDUSTRIAL AREA): +254 (20) 5550360</div>
    <div>FAX (TOWN OFFICE): +254 (20) 5550718 EMAIL: info@voltridgepower.example</div>
  </div>

  <div class="panels">
    <div class="panel-photo mcc" role="img" aria-label="Photo of an open MCC panel with a variable speed drive on an orange backplate"></div>
    <div class="panel-photo pcc" role="img" aria-label="Photo of an open grey PCC panel with meter and breakers"></div>
    <div class="panel-photo automation" role="img" aria-label="Photo of open automation panel cabinets with PLC modules"></div>
    <div class="caption mcc">MCC Panel with VSD</div>
    <div class="caption pcc">PCC Panel</div>
    <div class="caption automation">Automation Panel</div>
  </div>

  <svg class="analysis-chart" viewBox="0 0 606 351" role="img" aria-label="Power quality analysis line charts for L1, L2, L3 and total">
    <defs>
      <g id="trace-set" fill="none" stroke-width="1">
        <rect x="0" y="0" width="520" height="80" fill="#fff" stroke="#000" stroke-width=".8"/>
        <g stroke="var(--grid)" stroke-dasharray="2 2" stroke-width=".4">
          <line x1="0" y1="16" x2="520" y2="16"/><line x1="0" y1="32" x2="520" y2="32"/>
          <line x1="0" y1="48" x2="520" y2="48"/><line x1="0" y1="64" x2="520" y2="64"/>
          <line x1="80" y1="0" x2="80" y2="80"/><line x1="220" y1="0" x2="220" y2="80"/>
          <line x1="360" y1="0" x2="360" y2="80"/><line x1="500" y1="0" x2="500" y2="80"/>
        </g>
        <polyline stroke="var(--line-cyan)" points="0,44 40,42 80,46 150,44 155,50 200,52 300,50 400,50 460,48 520,46"/>
        <polyline stroke="var(--line-magenta)" points="0,40 30,38 40,46 60,36 100,40 150,40 152,74 156,46 200,50 260,48 320,48 400,46 460,44 500,38 520,40"/>
        <polyline stroke="var(--line-brown)" points="0,30 25,30 35,40 45,28 80,34 120,30 150,34 152,72 156,38 180,42 200,46 260,44 320,44 400,42 460,40 500,30 520,32"/>
        <polyline stroke="var(--line-green)" points="0,24 20,22 30,34 40,22 80,26 120,24 150,26 152,70 156,30 175,32 200,38 240,36 300,38 320,30 330,37 400,36 440,32 480,28 500,22 520,24"/>
        <g stroke="var(--line-green)" stroke-width="1.4">
          <line x1="62" y1="10" x2="62" y2="30"/><line x1="240" y1="12" x2="240" y2="38"/>
          <line x1="330" y1="14" x2="330" y2="38"/><line x1="396" y1="12" x2="396" y2="36"/>
          <line x1="470" y1="14" x2="470" y2="34"/>
        </g>
        <polyline stroke="var(--line-blue)" points="0,14 40,13 80,15 120,12 150,12 160,20 170,12 260,11 300,12 360,12 420,12 460,14 500,10 520,9"/>
      </g>
    </defs>
    <g transform="translate(40,2)"><use href="#trace-set"/><line x1="146" y1="0" x2="146" y2="80" stroke="#000" stroke-width="1.4"/></g>
    <g transform="translate(40,84)"><use href="#trace-set"/></g>
    <g transform="translate(40,166)"><use href="#trace-set"/></g>
    <g transform="translate(40,248)"><use href="#trace-set"/></g>
    <g class="chart-text">
      <text x="10" y="45" transform="rotate(-90 10 45)" text-anchor="middle">L1 (kW, kVAR)</text>
      <text x="10" y="127" transform="rotate(-90 10 127)" text-anchor="middle">L2 (kW, kVAR)</text>
      <text x="10" y="209" transform="rotate(-90 10 209)" text-anchor="middle">L3 (kW, kVAR)</text>
      <text x="10" y="291" transform="rotate(-90 10 291)" text-anchor="middle">Total (kW, kVAR)</text>
      <text x="598" y="45" transform="rotate(90 598 45)" text-anchor="middle">L1 (PF)</text>
      <text x="598" y="127" transform="rotate(90 598 127)" text-anchor="middle">L2 (PF)</text>
      <text x="598" y="209" transform="rotate(90 598 209)" text-anchor="middle">L3 (PF)</text>
      <text x="598" y="291" transform="rotate(90 598 291)" text-anchor="middle">Total (PF)</text>
      <text x="36" y="5" text-anchor="end">100</text><text x="36" y="21" text-anchor="end">76</text><text x="36" y="37" text-anchor="end">52</text><text x="36" y="53" text-anchor="end">28</text><text x="36" y="69" text-anchor="end">4</text><text x="36" y="84" text-anchor="end">-20</text>
      <text x="36" y="169" text-anchor="end">100</text><text x="36" y="185" text-anchor="end">76</text><text x="36" y="201" text-anchor="end">52</text><text x="36" y="217" text-anchor="end">28</text><text x="36" y="233" text-anchor="end">4</text>
      <text x="36" y="251" text-anchor="end">300</text><text x="36" y="267" text-anchor="end">220</text><text x="36" y="283" text-anchor="end">140</text><text x="36" y="299" text-anchor="end">60</text><text x="36" y="315" text-anchor="end">-20</text><text x="36" y="331" text-anchor="end">-100</text>
      <text x="564" y="5">1</text><text x="564" y="21">0.84</text><text x="564" y="37">0.68</text><text x="564" y="53">0.52</text><text x="564" y="69">0.36</text><text x="564" y="84">0.2</text>
      <text x="564" y="267">0.76</text><text x="564" y="283">0.52</text><text x="564" y="299">0.28</text><text x="564" y="315">0.04</text><text x="564" y="331">-0.2</text>
      <text x="120" y="338" text-anchor="middle">16-2 12h</text><text x="260" y="338" text-anchor="middle">16-2 18h</text>
      <text x="400" y="338" text-anchor="middle">17-2 0h</text><text x="540" y="338" text-anchor="middle">17-2 6h</text>
    </g>
  </svg>
  <div class="analysis-caption">Power Quality Analysis</div>

  <div class="footer-band">
    <div class="footer-label">COMPANY PROFILE<span class="sep">|</span><b>05</b></div>
  </div>
</div>
</body>
</html>
```